Engineering Consultant Business Card

I'm starting a new business as a high-end engineering consultant in a niche field. I've attached the jpg for my logo plus the branding guideline document that I've been following. You can see my business website here: www.tarvikworks.com
I'd like a business card that has the logo on one side, then the other side has (in any order): Tarvik Works, Inc.
Dana Whitlock
President and Chief EMC Engineer
www.tarvikworks.com
dana@tarvikworks.com
Optional: motto "We will solve your EMC problems as early as possible—ideally before they even start."
I'm not planning on including a phone number
Target Market(s)
Businesses, especially makers of electronics hardware
Industry/Entity Type
Electrical engineering
Contact Information for Business Card
Company name, my name, website, email

```html
<!DOCTYPE html>
<html lang="en">
<head>
<meta charset="utf-8">
<title>Tarvik Works, Inc. – Business Card</title>
<link href="https://fonts.googleapis.com/css2?family=Montserrat:wght@400;500;600;700&display=swap" rel="stylesheet">
<style>
  :root {
    --brand-blue: #2d45a0;
    --paper: #ffffff;
    --ink: #111111;
    --backdrop: #979b9f;
  }
  * { margin: 0; padding: 0; box-sizing: border-box; }
  html, body {
    width: 1200px; height: 1200px; overflow: hidden;
    background: var(--backdrop);
    font-family: "Montserrat", sans-serif;
  }
  .canvas { position: relative; width: 1200px; height: 1200px; }

  .card {
    position: absolute;
    left: 292px;
    width: 623px;
    height: 402px;
    overflow: hidden;
  }
  .card--front { top: 178px; background: var(--brand-blue); }
  .card--back  { top: 654px; background: var(--paper); }

  /* Front: brand name as wordmark stand-in */
  .front-brand {
    position: absolute; inset: 0;
    display: flex; align-items: center; justify-content: center; gap: 16px;
    color: var(--paper);
    font-weight: 700; font-size: 40px; letter-spacing: 0.5px;
  }
  .brand-dot {
    width: 26px; height: 26px; border-radius: 50%;
    background: var(--paper);
  }

  /* Back */
  .back-brand {
    position: absolute; top: 70px; left: 0; right: 0;
    display: flex; align-items: center; justify-content: center; gap: 10px;
    color: var(--brand-blue);
    font-weight: 700; font-size: 30px;
  }
  .back-brand .brand-dot { width: 18px; height: 18px; background: var(--brand-blue); }

  .company-name {
    position: absolute; top: 144px; left: 0; right: 0;
    text-align: center; color: var(--ink);
    font-weight: 600; font-size: 21px;
  }
  .divider {
    position: absolute; top: 195px; left: 280px;
    width: 63px; height: 2px; background: var(--brand-blue);
  }
  .person-name {
    position: absolute; top: 226px; left: 0; right: 0;
    text-align: center; color: var(--brand-blue);
    font-weight: 600; font-size: 21px;
  }
  .person-title {
    position: absolute; top: 256px; left: 0; right: 0;
    text-align: center; color: var(--ink);
    font-weight: 400; font-size: 15.5px;
  }

  .contact-band {
    position: absolute; left: 0; right: 0; bottom: 0; height: 88px;
    background: var(--brand-blue); color: var(--paper);
    font-size: 15.5px; font-weight: 400;
  }
  .contact {
    position: absolute; top: 0; height: 88px;
    display: flex; align-items: center; gap: 12px;
  }
  .contact--email { left: 35px; }
  .contact--web { right: 35px; }
  .contact svg { display: block; }
</style>
</head>
<body>
<main class="canvas">

  <section class="card card--front" aria-label="Card front">
    <div class="front-brand"><span class="brand-dot"></span>Tarvik Works</div>
  </section>

  <section class="card card--back" aria-label="Card back">
    <div class="back-brand"><span class="brand-dot"></span>Tarvik Works</div>
    <h1 class="company-name">Tarvik Works, Inc</h1>
    <div class="divider"></div>
    <h2 class="person-name">Dana Whitlock</h2>
    <p class="person-title">(President and Chief EMC Engineer)</p>

    <footer class="contact-band">
      <div class="contact contact--email">
        <svg width="20" height="14" viewBox="0 0 20 14" aria-hidden="true">
          <rect x="0.5" y="0.5" width="19" height="13" fill="#fff"/>
          <path d="M0.5 0.5 L10 8 L19.5 0.5 M0.5 13.5 L7.5 6.5 M19.5 13.5 L12.5 6.5" stroke="#2d45a0" stroke-width="1.2" fill="none"/>
        </svg>
        <span>dana@tarvikworks.com</span>
      </div>
      <div class="contact contact--web">
        <span>www.tarvikworks.com</span>
        <svg width="20" height="20" viewBox="0 0 20 20" aria-hidden="true">
          <circle cx="9" cy="9" r="8" fill="none" stroke="#fff" stroke-width="1.8"/>
          <ellipse cx="9" cy="9" rx="3.5" ry="8" fill="none" stroke="#fff" stroke-width="1.4"/>
          <line x1="1" y1="9" x2="17" y2="9" stroke="#fff" stroke-width="1.4"/>
          <path d="M11 11 L11 19.5 L13.3 17.3 L15.2 20 L16.6 19.2 L14.8 16.6 L18 16.2 Z" fill="#fff" stroke="#2d45a0" stroke-width="0.8"/>
        </svg>
      </div>
    </footer>
  </section>

</main>
</body>
</html>
```